Medigap Insurance Interactive website

We are looking at redesigning our website for a more up to date and responsive look and feel. We will code this site using Bootstrap 3 so please research and know how to design for this. Attached is our logo and a wireframe for the new site.
I look forward to seeing what you guys can do.

Target Market(s)

People elegible for Medigap Insurance in the US

Industry/Entity Type

Insurance

Number of Pages Required

5+ page

Font styles to use
Sans Serif

Requirements
Must have
• Match the logo
• Be Bootstrap 3 compatible design
• Font Awesome Icons

```html
<!DOCTYPE html>
<html lang="en">
<head>
<meta charset="utf-8">
<title>Harborline – Medicare Supplement Plans</title>
<link rel="stylesheet" href="https://fonts.googleapis.com/css2?family=Lato:wght@400;700&family=Oswald:wght@400;500&family=Crimson+Text:wght@400;600&display=swap">
<style>
:root{
  --red:#b71c1c;
  --red-bright:#c62828;
  --navy:#0b2d6b;
  --navy-deep:#062a63;
  --ink:#222;
  --text:#333;
  --muted:#777;
  --line:#e2e2e2;
  --white:#fff;
}
*{box-sizing:border-box;margin:0;padding:0}
html,body{width:1176px;height:1200px;overflow:hidden;background:var(--white)}
body{font-family:'Lato',sans-serif;color:var(--text);position:relative}
.wrap{position:absolute;left:97px;width:982px}

/* top bar */
.topbar{position:absolute;top:0;left:0;width:1176px;height:32px;background:#fafafa;border-bottom:1px solid #eee}
.topbar .call{position:absolute;left:97px;top:6px;font-size:11px;color:var(--red);text-transform:uppercase;display:flex;align-items:center;gap:5px}
.topbar .call strong{font-family:'Oswald',sans-serif;font-weight:400;font-size:18px;color:var(--navy);letter-spacing:-.2px}
.social{position:absolute;right:97px;top:5px;display:flex;gap:7px}
.social span{width:21px;height:21px;border:1.6px solid var(--red);border-radius:50%}

/* header */
.header{position:absolute;top:32px;left:0;width:1176px;height:56px}
.header svg{position:absolute;left:0;top:0}
.brand{position:absolute;left:97px;top:16px;font-family:'Lato',sans-serif;font-weight:700;font-size:20px;color:var(--navy);letter-spacing:.5px;line-height:24px}
.nav{position:absolute;left:376px;top:22px;display:flex;gap:27px}
.nav a{color:var(--white);text-decoration:none;font-size:10.5px;font-weight:700;letter-spacing:.1px}

/* hero */
.hero{position:absolute;top:88px;left:0;width:1176px;height:521px;overflow:hidden}
.hero-photo{position:absolute;inset:0;background:radial-gradient(ellipse at 30% 40%,#e8d8c8 0%,#c9c39a 30%,#9fae3c 60%,#6d8a20 100%)}
.hero-caption{position:absolute;left:0;top:274px;width:624px;height:176px;background:rgba(255,255,255,.72)}
.hero-caption h1{position:absolute;left:97px;top:12px;font-family:'Oswald',sans-serif;font-weight:400;font-size:36px;line-height:54px;color:#111;letter-spacing:-.6px}
.video{position:absolute;left:624px;top:113px;width:454px;height:336px;background:linear-gradient(160deg,#4a4a4a,#333);box-shadow:0 14px 18px -10px rgba(0,0,0,.5)}
.video .play{position:absolute;left:197px;top:139px}
.dots{position:absolute;left:549px;top:490px;display:flex;gap:9px}
.dots span{width:13px;height:13px;border:1.6px solid var(--navy);border-radius:50%}
.dots span.on{background:var(--navy)}

/* feature tiles */
.tiles{top:653px;display:flex;justify-content:space-between}
.tile{width:218px;height:134px;position:relative;display:flex;flex-direction:column;align-items:center;box-shadow:inset 0 0 14px rgba(0,0,0,.25)}
.tile.red{background:var(--red-bright)}
.tile.blue{background:var(--navy-deep)}
.tile svg{margin-top:20px}
.tile .label{position:absolute;bottom:0;left:0;right:0;height:38px;background:rgba(0,0,0,.08);font-family:'Crimson Text',serif;font-weight:600;font-size:18px;letter-spacing:.3px;color:var(--white);text-align:center;line-height:38px}
.divider{position:absolute;top:828px;left:200px;width:776px;height:1px;background:linear-gradient(90deg,transparent,#ddd,transparent)}

/* info columns */
.info{top:866px;display:flex;gap:39px}
.col{width:302px}
.col h2{font-family:'Crimson Text',serif;font-weight:400;font-size:28px;color:var(--navy);line-height:36px;padding-bottom:8px;border-bottom:1px solid var(--red);position:relative}
.col h2 em{font-style:normal;color:var(--red)}
.col h2::after{content:"";position:absolute;left:0;bottom:-2px;width:44px;height:3px;background:var(--navy)}
.col p{font-size:11.5px;line-height:19.7px;margin-top:12px;color:var(--text)}
.more{display:block;margin-top:11px;font-size:11.5px;color:var(--red);text-decoration:none}
.quote{margin-top:18px;border:1px solid #eee;border-radius:3px;padding:10px 16px 12px 38px;position:relative;font-style:italic;font-size:12px;line-height:17.6px;color:var(--muted);text-align:center}
.quote .mark{position:absolute;left:8px;top:-4px;font-family:'Crimson Text',serif;font-size:48px;line-height:48px;color:#ccc;font-style:normal}
.author{font-size:12px;color:var(--ink);margin:6px 0 0 70px;letter-spacing:.3px}
.qdots{display:flex;gap:10px;margin-top:15px}
.qdots span{width:8px;height:8px;border:1.4px solid var(--red);border-radius:50%}
.qdots span.on{background:var(--red)}
.email{margin-top:8px;width:302px;height:39px;border:1px solid #e6e6e6;padding:0 10px;font-size:11px;color:#888;line-height:39px;letter-spacing:.3px}
.signup{margin-top:10px;width:118px;height:38px;background:var(--red);color:var(--white);font-size:11.5px;font-weight:700;text-align:center;line-height:38px}

/* footer */
.footer{position:absolute;top:1105px;left:0;width:1176px;height:95px;background:var(--navy-deep);text-align:center;color:var(--white)}
.footer nav{margin-top:24px;display:flex;justify-content:center;gap:41px}
.footer nav a{color:var(--white);text-decoration:none;font-size:12.5px;letter-spacing:.3px}
.footer small{display:block;margin-top:18px;font-size:11px}
</style>
</head>
<body>

<div class="topbar">
  <div class="call">Compare rates and save : <strong>(800) 555-0142</strong></div>
  <div class="social" aria-label="Social links"><span></span><span></span><span></span><span></span></div>
</div>

<header class="header">
  <svg width="1176" height="56" aria-hidden="true">
    <path d="M316 0 H1176 V56 H367 C360 30 345 8 316 0 Z" fill="var(--red-bright)"/>
    <path d="M600 56 C800 30 950 60 1176 30 V56 Z" fill="#a91616" opacity=".5"/>
  </svg>
  <div class="brand">HARBORLINE</div>
  <nav class="nav">
    <a href="#">MEDICARE SUPPLEMENT</a><a href="#">PART D</a><a href="#">HOW TO DECIDE</a><a href="#">LEARN ONLINE</a><a href="#">WHY HARBORLINE</a><a href="#">BUY NOW</a>
  </nav>
</header>

<section class="hero">
  <div class="hero-photo" role="img" aria-label="Photo of a smiling senior couple outdoors in a sunny green park"></div>
  <div class="hero-caption">
    <h1>Medicare Supplement Insurance Plan<br>Comparison from Top Medigap<br>Insurance Companies</h1>
  </div>
  <div class="video" role="img" aria-label="Video preview showing the zip code rate comparison tool">
    <svg class="play" width="60" height="60" aria-hidden="true"><circle cx="30" cy="30" r="29" fill="#d61a1a"/><path d="M24 18 L42 30 L24 42 Z" fill="#222"/></svg>
  </div>
  <div class="dots"><span class="on"></span><span></span><span></span><span></span></div>
</section>

<section class="wrap tiles">
  <div class="tile red">
    <svg width="76" height="60" viewBox="0 0 76 60" aria-hidden="true"><path d="M0 14h28V4l18 16-18 16V26H0z" fill="#fff"/><path d="M76 34H48V24L30 40l18 16V46h28z" fill="#fff"/></svg>
    <div class="label">COMPARE RATES</div>
  </div>
  <div class="tile blue">
    <svg width="72" height="60" viewBox="0 0 72 60" aria-hidden="true"><path d="M2 4h10l10 36h40l8-28H16" fill="none" stroke="#fff" stroke-width="6" stroke-linejoin="round"/><path d="M20 22h46M24 31h38M36 14v26M50 14v26" stroke="#fff" stroke-width="3"/><circle cx="28" cy="52" r="6" fill="#fff"/><circle cx="56" cy="52" r="6" fill="#fff"/></svg>
    <div class="label">BUY NOW</div>
  </div>
  <div class="tile red">
    <svg width="60" height="60" viewBox="0 0 60 60" aria-hidden="true"><circle cx="30" cy="30" r="27" fill="none" stroke="#fff" stroke-width="4"/><path d="M25 16l14 14-14 14" fill="none" stroke="#fff" stroke-width="4"/></svg>
    <div class="label">LEARN MORE</div>
  </div>
  <div class="tile blue">
    <svg width="60" height="62" viewBox="0 0 60 62" aria-hidden="true"><circle cx="30" cy="16" r="14" fill="#fff"/><path d="M3 62c0-18 10-26 27-26s27 8 27 26z" fill="#fff"/><path d="M27 36h6l-3 18z" fill="var(--navy-deep)"/></svg>
    <div class="label">GET EXPERT HELP</div>
  </div>
</section>

<div class="divider"></div>

<section class="wrap info">
  <div class="col">
    <h2><em>Welcome to</em> Harborline</h2>
    <p>Lorem ipsum dolor sit amet, consectetuer adipiscinelit, sed diam nonummy nibh euismod tincidunt ut la dolore magna aliquam erat volutpat. Ut wisi enim ad veniam, quis nostrud exerci tation ullamcorper suscipit lobortis nisl ut aliqu ex ea commodo consequat. Duis autem vel eudolor in hendrerit in vulputate velit esse molestie consequat.</p>
    <a class="more" href="#">READ MORE</a>
  </div>
  <div class="col">
    <h2><em>What People</em> are Saying</h2>
    <div class="quote"><span class="mark">“</span>Lorem ipsum dolor sit amet, consectetuer adipiscing elit, sed diam nonummy nibh euismod tincidunt ut laoreet dolore magna aliquam erat volutpat.</div>
    <div class="author">Mr. Paul Brennan</div>
    <div class="qdots"><span class="on"></span><span></span><span></span><span></span></div>
  </div>
  <div class="col">
    <h2><em>Monthly</em> Updates</h2>
    <p>Enter Email for customized Monthly Rate Update and More...</p>
    <div class="email">Enter Your Email</div>
    <div class="signup">SIGN UP</div>
  </div>
</section>

<footer class="footer">
  <nav><a href="#">Harborline</a><a href="#">Sitemap</a><a href="#">Buy Now</a><a href="#">Blog</a><a href="#">Login</a></nav>
  <small>© 2014 HARBORLINE. All rights reserved.</small>
</footer>

</body>
</html>
```